Plakat-Design für eine Werbeschild für ein Geflügelhof
Zielgruppe
Wir sind ein Geflügelhof, Landhandel, Hofladen, Eier stehen seit über 100 Jahren für Hof Kranwede, artgerechte Tierhaltung und Artikelvielfalt machen uns bekannt.
Aufgabenstellung
Das Werbeschild wird auf dem Hof aufgestellt und soll den Weg zum Hof zeigen.
- die Maße vom Schild: 1,50m breit x 2,40m hoch
- Grafiken werden als .ai und .pdf benötigt
- Logo ist hochgelagen
- Foto von unserer Vorstellung ist hochgeladen
Das Schild muss 400 m RECHTS drauf gedruckt haben.
Falls es zu breit wäre, könnte das Logo ja vielleicht auch über Hof Kranwede.
Das ganze wird bei plattenwerk auf eine MetoxPan-Platte in den Druck gegeben.

```html
<!DOCTYPE html>
<html lang="de">
<head>
<meta charset="utf-8">
<title>Hof Kranwede – Wegweiser</title>
<link rel="stylesheet" href="https://fonts.googleapis.com/css2?family=Kalam:wght@700&display=swap">
<style>
  :root {
    --page: #ffffff;
    --sign: #ffffff;
    --grass: #2a7023;
    --grass-light: #4f9a3f;
    --animal: #595959;
    --ink: #000000;
    --signal: #cc1417;
  }
  html, body {
    margin: 0;
    padding: 0;
    width: 848px;
    height: 1200px;
    overflow: hidden;
    background: var(--page);
  }
  .canvas {
    position: relative;
    width: 848px;
    height: 1200px;
    font-family: "Kalam", "Comic Sans MS", cursive;
  }
  .sign {
    position: absolute;
    left: 123px;
    top: 117px;
    width: 614px;
    height: 983px;
    background: var(--sign);
    overflow: hidden;
  }
  .meadow-top {
    position: absolute;
    left: 0;
    top: 38px;
    width: 614px;
    height: 112px;
    background: linear-gradient(to bottom, rgba(89,89,89,0) 0%, rgba(89,89,89,0.18) 45%, var(--grass-light) 78%, var(--grass) 100%);
  }
  .meadow-top-band {
    position: absolute;
    left: 0;
    top: 148px;
    width: 614px;
    height: 11px;
    background: var(--grass);
  }
  .farm-name {
    position: absolute;
    left: 0;
    top: 178px;
    width: 614px;
    margin: 0;
    text-align: center;
    font-size: 80px;
    font-weight: 700;
    line-height: 1;
    color: var(--grass);
    letter-spacing: -1px;
  }
  .headline {
    position: absolute;
    left: 0;
    top: 305px;
    width: 614px;
    margin: 0;
    text-align: center;
    font-size: 92px;
    font-weight: 700;
    line-height: 87px;
    color: var(--ink);
    letter-spacing: -1px;
  }
  .distance {
    position: absolute;
    left: 0;
    top: 602px;
    width: 614px;
    margin: 0;
    text-align: center;
    font-size: 94px;
    font-weight: 700;
    line-height: 1;
    color: var(--signal);
  }
  .direction-arrow {
    position: absolute;
    left: 86px;
    top: 690px;
    width: 445px;
    height: 70px;
  }
  .meadow-bottom {
    position: absolute;
    left: 0;
    top: 800px;
    width: 614px;
    height: 183px;
    background: linear-gradient(to bottom, rgba(89,89,89,0) 0%, rgba(89,89,89,0.45) 30%, var(--animal) 55%, var(--grass-light) 80%, var(--grass) 100%);
  }
</style>
</head>
<body>
<div class="canvas">
  <section class="sign">
    <div class="meadow-top" role="img" aria-label="Ente und Huhn als Silhouetten auf einer grünen Wiese"></div>
    <div class="meadow-top-band"></div>

    <h1 class="farm-name">Hof Kranwede</h1>

    <p class="headline">Einkauf<br>auf dem<br>Bauernhof</p>

    <p class="distance">400 m rechts</p>

    <svg class="direction-arrow" viewBox="0 0 445 70" aria-hidden="true">
      <path d="M2 30 L300 24 L440 27" fill="none" stroke="var(--signal)" stroke-width="6" stroke-linecap="round"/>
      <path d="M30 33 L300 28 L420 30" fill="none" stroke="var(--signal)" stroke-width="4" stroke-linecap="round"/>
      <path d="M345 4 L440 22 L360 66" fill="none" stroke="var(--signal)" stroke-width="6" stroke-linecap="round" stroke-linejoin="round"/>
      <path d="M350 10 L432 26 L352 58" fill="none" stroke="var(--signal)" stroke-width="3" stroke-linecap="round" stroke-linejoin="round"/>
    </svg>

    <div class="meadow-bottom" role="img" aria-label="Schwein, Kaninchen und Kalb als Silhouetten auf einer grünen Wiese"></div>
  </section>
</div>
</body>
</html>
```